Muffintop Studio print Advertisement

We are a new online-based store searching for an awesome print advertisement design to use in all our current and future ads. We need an ad that pops and to prompt readers to visit my website (and make a purchase).

Somewhere on the ad, I would like a small section where I can easily change out coupon codes so I can easily differentiate where our marketing effort succeed.

If you think there are any photos on our website that is better suited for the ad, please let us know and we'll post it up here for you to use!

Ad size should be 2.1875"width (656px) x 2.8"height (840px).

www.muffintopstudio-example.com

Target Market(s)

Female age 16 to 40.

Requirements
Must have
• Section where we can put coupon code.

```html
<!DOCTYPE html>
<html lang="en">
<head>
<meta charset="utf-8">
<title>Muffintop Studio – Print Advertisement</title>
<link rel="stylesheet" href="https://fonts.googleapis.com/css2?family=Sniglet:wght@400;800&family=PT+Sans+Narrow:wght@700&family=Yanone+Kaffeesatz:wght@700&family=Open+Sans:wght@700&display=swap">
<style>
  :root {
    --frame-brown: #6e5140;
    --paper: #ffffff;
    --headline-purple: #4a1858;
    --headline-glow: #e9d6ef;
    --brand-pink: #e8748f;
    --action-green: #2f7a17;
    --url-green: #1f6a12;
    --coupon-fill: #fdfbd9;
    --coupon-edge: #e9e3a8;
  }
  * { box-sizing: border-box; margin: 0; padding: 0; }
  html, body { width: 937px; height: 1200px; overflow: hidden; }
  body { background: var(--paper); }
  .ad {
    position: relative;
    width: 937px;
    height: 1200px;
    background: var(--paper);
    overflow: hidden;
  }
  .ad::after {
    content: "";
    position: absolute;
    inset: 0;
    box-shadow: inset 0 0 70px 26px var(--frame-brown);
    pointer-events: none;
  }
  .photo-column {
    position: absolute;
    left: 0;
    top: 0;
    width: 340px;
    height: 940px;
  }
  .headline {
    position: absolute;
    left: 270px;
    top: 34px;
    width: 660px;
    text-align: center;
    font-family: "Sniglet", "Comic Sans MS", sans-serif;
    font-weight: 400;
    font-size: 86px;
    line-height: 92px;
    color: var(--headline-purple);
    text-shadow: 0 0 3px var(--headline-glow), 0 0 3px var(--headline-glow);
  }
  .brand {
    position: absolute;
    left: 330px;
    top: 640px;
    width: 540px;
    display: flex;
    align-items: center;
    justify-content: center;
    gap: 22px;
    font-family: "Sniglet", "Comic Sans MS", sans-serif;
    font-weight: 400;
    font-size: 100px;
    line-height: 104px;
    color: var(--brand-pink);
  }
  .brand-dot {
    width: 48px;
    height: 48px;
    border-radius: 50%;
    background: var(--brand-pink);
    flex: none;
  }
  .brand-name { text-align: center; }
  .call-to-action {
    position: absolute;
    right: 40px;
    top: 925px;
    font-family: "Yanone Kaffeesatz", "PT Sans Narrow", sans-serif;
    font-weight: 700;
    font-size: 72px;
    line-height: 80px;
    color: var(--action-green);
    white-space: nowrap;
  }
  .web-address {
    position: absolute;
    left: 30px;
    right: 40px;
    top: 995px;
    text-align: center;
    font-family: "PT Sans Narrow", "Arial Narrow", sans-serif;
    font-weight: 700;
    font-size: 68px;
    line-height: 80px;
    color: var(--url-green);
    white-space: nowrap;
  }
  .coupon {
    position: absolute;
    left: 458px;
    top: 1090px;
    width: 454px;
    height: 90px;
  }
  .coupon-label {
    position: absolute;
    left: 612px;
    top: 1088px;
    font-family: "Open Sans", Arial, sans-serif;
    font-weight: 700;
    font-size: 20px;
    color: #111;
  }
</style>
</head>
<body>
  <main class="ad">
    <svg class="photo-column" viewBox="0 0 340 940" role="img" aria-label="Three product photographs: a yellow giraffe cable clip wound on a white cord, a woman with blonde curls wearing a white cord accessory, and travel-themed stickers on a wooden table">
      <defs>
        <radialGradient id="photoClip" cx="0.4" cy="0.4" r="0.8">
          <stop offset="0" stop-color="#f0c25a"/>
          <stop offset="0.3" stop-color="#e9cfa6"/>
          <stop offset="0.7" stop-color="#d9c3b0"/>
          <stop offset="1" stop-color="#b9c7a8"/>
        </radialGradient>
        <radialGradient id="photoPortrait" cx="0.35" cy="0.45" r="0.8">
          <stop offset="0" stop-color="#f1d9c8"/>
          <stop offset="0.5" stop-color="#f6ebe0"/>
          <stop offset="1" stop-color="#fbf6ef"/>
        </radialGradient>
        <radialGradient id="photoStickers" cx="0.5" cy="0.5" r="0.8">
          <stop offset="0" stop-color="#ecd7b9"/>
          <stop offset="0.5" stop-color="#f3e6d2"/>
          <stop offset="1" stop-color="#fbf5ec"/>
        </radialGradient>
      </defs>
      <path d="M0 0 H310 L295 45 318 90 300 140 322 190 305 235 318 270 270 285 220 300 160 282 100 305 40 290 0 300 Z" fill="url(#photoClip)"/>
      <path d="M0 305 L40 295 100 312 160 288 220 305 270 292 312 284 300 330 325 380 305 430 330 480 312 530 332 585 310 625 250 640 190 622 130 650 70 630 0 650 Z" fill="url(#photoPortrait)"/>
      <path d="M0 658 L70 638 130 658 190 630 250 648 312 632 296 680 318 725 300 775 322 825 300 870 316 910 280 930 0 930 Z" fill="url(#photoStickers)"/>
    </svg>

    <h1 class="headline">Innovative- Fun<br>Modern Crafts<br>&amp; accessories for<br>you, friends,<br>&amp; home!</h1>

    <div class="brand"><span class="brand-dot"></span><span class="brand-name">Muffintop<br>Studio</span></div>

    <p class="call-to-action">Order up some Fun Today!</p>
    <p class="web-address">www.muffintopstudio-example.com</p>

    <svg class="coupon" viewBox="0 0 454 90" aria-hidden="true">
      <path d="M14 28 H128 L138 4 L160 28 H440 Q450 28 450 38 V78 Q450 88 440 88 H14 Q4 88 4 78 V38 Q4 28 14 28 Z" fill="var(--coupon-fill)" stroke="var(--coupon-edge)" stroke-width="2"/>
    </svg>
    <span class="coupon-label">Coupon Code</span>
  </main>
</body>
</html>
```